Business Card Design Project

Want a modern business card.
Concern is that our email address is long and thus poses a design challenge.
Items like the company name can be omitted from text as it will be available via the logo.

Example:
Gerald Tunstall
President / CEO
Cell 555.304.1182
Office 555.617.2093
geraldt@korvantsolutionsgroup.example
www.korvantsolutionsgroup.example

Target Market(s)

Technical and executive level members of Information Technology companies in the Healthcare industry.

Industry/Entity Type

Business

Colors

Designer to choose colors to be used in the design.

Requirements
Nice to have
• Raised logo, but I am open.

```html
<!DOCTYPE html>
<html lang="en">
<head>
<meta charset="utf-8">
<title>Korvant Solutions Group — Business Card</title>
<link rel="stylesheet" href="https://fonts.googleapis.com/css2?family=Cinzel:wght@700&family=Arimo:wght@400&display=swap">
<style>
  :root {
    --navy: #1b2a80;
    --red: #e0141b;
    --white: #ffffff;
    --paper: #f7f7f7;
    --backdrop: #e9e6e2;
    --ink: #1b2a80;
  }
  * { box-sizing: border-box; margin: 0; padding: 0; }
  html, body { width: 1200px; height: 960px; overflow: hidden; }
  body {
    background: var(--backdrop);
    font-family: "Arimo", Arial, sans-serif;
    position: relative;
  }
  .card {
    position: absolute;
    left: 250px;
    width: 700px;
    height: 400px;
    box-shadow: 0 6px 18px rgba(0,0,0,0.18);
    overflow: hidden;
  }
  .card--back { top: 48px; background: var(--navy); }
  .card--front { top: 512px; background: linear-gradient(180deg, var(--white), var(--paper)); }

  .wordmark {
    font-family: "Cinzel", Georgia, serif;
    font-weight: 700;
    line-height: 1;
    letter-spacing: 1px;
  }
  .card--back .wordmark {
    position: absolute;
    left: 0; right: 0; top: 172px;
    text-align: center;
    color: var(--white);
    font-size: 38px;
  }
  .card--front .wordmark {
    position: absolute;
    left: 60px; top: 78px;
    color: var(--navy);
    font-size: 36px;
  }

  .rule { position: absolute; height: 3px; }
  .rule--blue { left: 0; width: 400px; top: 190px; background: var(--navy); }
  .rule--red { left: 590px; right: 0; top: 160px; background: var(--red); }

  .person { position: absolute; left: 412px; top: 146px; }
  .person__name { color: var(--navy); font-size: 24px; }
  .person__title { color: var(--red); font-size: 15px; margin-top: 4px; }

  .contact { position: absolute; list-style: none; color: var(--ink); font-size: 14px; }
  .contact li { display: flex; align-items: center; gap: 10px; height: 26px; }
  .contact svg { width: 14px; height: 14px; flex: none; }
  .contact--online { left: 60px; top: 268px; }
  .contact--phone { left: 430px; top: 228px; }

  .band { position: absolute; bottom: 0; height: 18px; }
  .band--blue { left: 0; width: 430px; background: var(--navy); }
  .band--red { left: 430px; right: 0; background: var(--red); }
</style>
</head>
<body>
  <section class="card card--back" aria-label="Card back">
    <div class="wordmark">Korvant Solutions Group</div>
  </section>

  <section class="card card--front" aria-label="Card front">
    <div class="wordmark">Korvant Solutions Group</div>

    <div class="rule rule--blue"></div>
    <div class="person">
      <div class="person__name">Gerald Tunstall</div>
      <div class="person__title">President / CEO</div>
    </div>
    <div class="rule rule--red"></div>

    <ul class="contact contact--phone">
      <li>
        <svg viewBox="0 0 14 14" aria-label="Cell"><circle cx="7" cy="4" r="3" fill="#e0141b"/><path d="M1 14c0-4 3-6 6-6s6 2 6 6z" fill="#e0141b"/></svg>
        555.304.1182
      </li>
      <li>
        <svg viewBox="0 0 14 14" aria-label="Office"><rect x="2" y="1" width="10" height="13" fill="#e0141b"/><rect x="4" y="3" width="2" height="2" fill="#fff"/><rect x="8" y="3" width="2" height="2" fill="#fff"/><rect x="4" y="7" width="2" height="2" fill="#fff"/><rect x="8" y="7" width="2" height="2" fill="#fff"/><rect x="6" y="11" width="2" height="3" fill="#fff"/></svg>
        555.617.2093
      </li>
    </ul>

    <ul class="contact contact--online">
      <li>
        <svg viewBox="0 0 14 14" aria-label="Web"><circle cx="7" cy="7" r="6.5" fill="#e0141b"/><path d="M0.5 7h13M7 0.5c-3 3.5-3 9.5 0 13M7 0.5c3 3.5 3 9.5 0 13" stroke="#fff" stroke-width="1" fill="none"/></svg>
        www.korvantsolutionsgroup.example
      </li>
      <li>
        <svg viewBox="0 0 14 14" aria-label="Email"><rect x="0.5" y="2.5" width="13" height="9" fill="#e0141b"/><path d="M0.5 2.5l6.5 5 6.5-5" stroke="#fff" stroke-width="1.2" fill="none"/></svg>
        geraldt@korvantsolutionsgroup.example
      </li>
    </ul>

    <div class="band band--blue"></div>
    <div class="band band--red"></div>
  </section>
</body>
</html>
```